app design for work order

Please refer to the image attached. I am not happy this current design. please re-design this page using your excellent taste. Our current app use white and grey color as main color. And use green (#8cc53e) and blue (#36a7c4) as additional case.

```html
<!DOCTYPE html>
<html lang="en">
<head>
<meta charset="utf-8">
<title>Work Order</title>
<link rel="stylesheet" href="https://fonts.googleapis.com/css2?family=Source+Sans+3:wght@400;500&display=swap">
<style>
:root{
  --green:#8cc53e;
  --blue:#36a7c4;
  --accent:#2b93b0;
  --icon:#7bb532;
  --ink:#2b2b2b;
  --muted:#4a4a4a;
  --line:#c4c4c4;
  --grey-bg:#f3f4f5;
  --white:#fff;
  --bar:#3a3d40;
  --grad:linear-gradient(90deg,var(--green),var(--blue));
}
*{margin:0;padding:0;box-sizing:border-box}
html,body{width:1200px;height:2583px;overflow:hidden;background:var(--white)}
body{position:relative;font-family:"Source Sans 3",sans-serif;color:var(--ink)}
.abs{position:absolute}
.status-bar{left:0;top:0;width:1200px;height:83px;background:var(--bar)}
.status-icons{right:40px;top:14px}
.app-header{left:7px;top:83px;width:1192px;height:180px;background:var(--grad);color:var(--white)}
.app-title{left:200px;top:46px;font-size:62px;font-weight:400}
.menu-icon{left:58px;top:56px}
.back-icon{right:32px;top:45px}
.toolbar-bg{left:0;top:263px;width:1200px;height:132px;background:var(--grey-bg)}
.toolbar .btn{position:absolute;top:284px;height:92px;border-radius:46px;display:flex;align-items:center;justify-content:center;color:var(--white);background:var(--grad)}
.btn-save{left:16px;width:261px;font-size:42px}
.btn-toggle{left:312px;width:189px;top:292px!important;height:75px!important}
.btn-toggle .knob{position:absolute;right:8px;top:8px;width:59px;height:59px;border-radius:50%;background:var(--white)}
.btn-mail{left:516px;width:213px;top:292px!important;height:75px!important}
.btn-actions{left:743px;width:217px;top:290px!important;height:79px!important;background:var(--white)!important;border:3px solid var(--blue);color:var(--ink)!important;font-size:30px}
.btn-submit{left:972px;width:213px;top:292px!important;height:75px!important;font-size:30px}
.entity-band{left:0;top:395px;width:1190px;height:141px;background:var(--grad);color:var(--white);font-size:51px;display:flex;align-items:center;justify-content:center}
.case-name{left:71px;top:590px;font-size:50px;color:var(--accent)}
.schedule{top:736px;font-size:43px;color:var(--ink);display:flex;align-items:center;gap:22px}
.schedule-start{left:60px}
.schedule-end{left:630px}
.section-band{left:5px;top:833px;width:1192px;height:135px;background:var(--grad);color:var(--white);font-size:60px;display:flex;align-items:center;justify-content:center}
.field-label{left:84px;font-size:50px;color:var(--accent);display:flex;align-items:center;gap:34px}
.field-label svg{width:48px;height:52px}
.field-input{left:66px;width:1088px;height:119px;border:2px solid var(--line);border-radius:60px;background:var(--white);box-shadow:3px 6px 6px rgba(0,0,0,.18);font-size:51px;color:var(--muted);padding-left:56px;display:flex;align-items:center}
.field-input .cal{position:absolute;right:56px;top:28px}
.bottom-nav{left:5px;top:2316px;width:1192px;height:184px;background:var(--grad);color:var(--white)}
.nav-item{position:absolute;top:38px;width:160px;margin-left:-80px;text-align:center;font-size:21px}
.nav-item svg{display:block;margin:0 auto 8px}
</style>
</head>
<body>
<div class="abs status-bar">
  <svg class="abs status-icons" width="260" height="56" viewBox="0 0 260 56">
    <g fill="none" stroke="#fff" stroke-width="6" stroke-linecap="round">
      <path d="M6 22a50 50 0 0 1 68 0"/><path d="M17 33a34 34 0 0 1 46 0"/><path d="M28 44a18 18 0 0 1 24 0"/>
    </g>
    <circle cx="40" cy="52" r="4" fill="#fff"/>
    <path d="M88 54L138 6V54Z" fill="#fff"/>
    <rect x="168" y="6" width="78" height="44" rx="6" fill="none" stroke="#fff" stroke-width="5"/>
    <rect x="246" y="18" width="8" height="20" fill="#fff"/>
    <rect x="176" y="14" width="14" height="28" fill="#fff"/><rect x="196" y="14" width="14" height="28" fill="#fff"/><rect x="216" y="14" width="14" height="28" fill="#fff"/>
  </svg>
</div>

<header class="abs app-header">
  <svg class="abs menu-icon" width="62" height="52" viewBox="0 0 62 52"><g fill="#fff"><rect width="62" height="10" rx="5"/><rect y="21" width="62" height="10" rx="5"/><rect y="42" width="62" height="10" rx="5"/></g></svg>
  <h1 class="abs app-title">Work Order</h1>
  <svg class="abs back-icon" width="96" height="76" viewBox="0 0 96 76"><g fill="none" stroke="#fff" stroke-width="8" stroke-linecap="round" stroke-linejoin="round"><path d="M90 38H8"/><path d="M38 6L6 38l32 32"/></g></svg>
</header>

<div class="abs toolbar-bg"></div>
<nav class="toolbar">
  <div class="btn btn-save">Save</div>
  <div class="btn btn-toggle"><span class="knob"></span></div>
  <div class="btn btn-mail"><svg width="66" height="46" viewBox="0 0 66 46"><g fill="none" stroke="#fff" stroke-width="4"><rect x="2" y="2" width="62" height="42"/><path d="M2 2l31 24L64 2M2 44l24-20M64 44L40 24"/></g></svg></div>
  <div class="btn btn-actions">Actions</div>
  <div class="btn btn-submit">Submit</div>
</nav>

<div class="abs entity-band">Entity Name: Kestrel Bank KTB Branch</div>
<div class="abs case-name">Case Name: Lorem Ipsum is simply...</div>

<div class="abs schedule schedule-start">
  <svg width="46" height="46" viewBox="0 0 46 46"><g fill="none" stroke="var(--icon)" stroke-width="4" stroke-linecap="round"><circle cx="23" cy="23" r="20"/><path d="M23 11v13h10"/></g></svg>
  <span>Start : 08-09-11&nbsp; 11:30</span>
</div>
<div class="abs schedule schedule-end">
  <svg width="86" height="64" viewBox="0 0 86 64"><g fill="none" stroke="var(--icon)" stroke-width="3.5" stroke-linecap="round" stroke-linejoin="round"><circle cx="58" cy="38" r="22"/><path d="M52 8h12M58 8v8M48 38l7 7 13-13M4 28h26M10 36h20M16 44h16M22 52h18"/></g></svg>
  <span>End : 08-09-11&nbsp; 11:30</span>
</div>

<div class="abs section-band">CSC Follow Up</div>

<div class="abs field-label" style="top:1014px">
  <svg viewBox="0 0 48 52"><g fill="var(--icon)"><circle cx="24" cy="13" r="12"/><path d="M2 52c0-16 9-24 22-24s22 8 22 24Z"/></g></svg>
  <span>Customer:</span>
</div>
<div class="abs field-input" style="top:1128px">Ned’s Test Customer Job 1</div>

<div class="abs field-label" style="top:1281px">
  <svg viewBox="0 0 48 52"><g fill="var(--icon)"><path d="M18 2h12l-3 8h-6Z"/><path d="M21 12h6l5 30-8 9-8-9Z"/></g><g stroke="#fff" stroke-width="2"><path d="M18 26l12-6M17 34l14-6"/></g></svg>
  <span>Job Code:</span>
</div>
<div class="abs field-input" style="top:1371px">####-#####-###</div>

<div class="abs field-label" style="top:1521px">
  <svg viewBox="0 0 48 52"><g fill="var(--icon)"><circle cx="24" cy="12" r="11"/><path d="M4 52c0-16 8-24 20-24s20 8 20 24Z"/></g><path d="M24 28l-4 8 4 12 4-12Z" fill="#fff"/><rect x="30" y="38" width="8" height="6" fill="#fff"/></svg>
  <span>Job Manager:</span>
</div>
<div class="abs field-input" style="top:1621px"></div>

<div class="abs field-label" style="top:1761px">
  <svg viewBox="0 0 48 52"><g fill="none" stroke="var(--icon)" stroke-width="3"><rect x="2" y="8" width="44" height="42"/><path d="M2 18h44M10 2v10M18 2v10M26 2v10M34 2v10"/></g><g fill="var(--icon)"><rect x="8" y="24" width="6" height="5"/><rect x="17" y="24" width="6" height="5"/><rect x="26" y="24" width="6" height="5"/><rect x="35" y="24" width="6" height="5"/><rect x="8" y="33" width="6" height="5"/><rect x="17" y="33" width="6" height="5"/><rect x="26" y="33" width="6" height="5"/><rect x="35" y="33" width="6" height="5"/><rect x="8" y="42" width="6" height="5"/><rect x="17" y="42" width="6" height="5"/><rect x="26" y="42" width="6" height="5"/></g></svg>
  <span>Created Date:</span>
</div>
<div class="abs field-input" style="top:1851px">
  <svg class="cal" width="60" height="64" viewBox="0 0 48 52"><g fill="none" stroke="#aaa" stroke-width="3"><rect x="2" y="8" width="44" height="42"/><path d="M2 18h44M10 2v10M18 2v10M26 2v10M34 2v10"/></g><g fill="#aaa"><rect x="8" y="24" width="6" height="5"/><rect x="17" y="24" width="6" height="5"/><rect x="26" y="24" width="6" height="5"/><rect x="35" y="24" width="6" height="5"/><rect x="8" y="34" width="6" height="5"/><rect x="17" y="34" width="6" height="5"/><rect x="26" y="34" width="6" height="5"/><rect x="35" y="34" width="6" height="5"/></g></svg>
</div>

<div class="abs field-label" style="top:2021px">
  <svg viewBox="0 0 48 52"><g fill="none" stroke="var(--icon)" stroke-width="3"><rect x="2" y="8" width="44" height="42"/><path d="M2 18h44M10 2v10M18 2v10M26 2v10M34 2v10"/></g><g fill="var(--icon)"><rect x="8" y="24" width="6" height="5"/><rect x="17" y="24" width="6" height="5"/><rect x="26" y="24" width="6" height="5"/><rect x="35" y="24" width="6" height="5"/><rect x="8" y="33" width="6" height="5"/><rect x="17" y="33" width="6" height="5"/><rect x="26" y="33" width="6" height="5"/><rect x="35" y="33" width="6" height="5"/><rect x="8" y="42" width="6" height="5"/><rect x="17" y="42" width="6" height="5"/><rect x="26" y="42" width="6" height="5"/></g></svg>
  <span>Ended&nbsp; Date:</span>
</div>
<div class="abs field-input" style="top:2107px;left:73px;width:1085px">
  <svg class="cal" width="60" height="64" viewBox="0 0 48 52"><g fill="none" stroke="#aaa" stroke-width="3"><rect x="2" y="8" width="44" height="42"/><path d="M2 18h44M10 2v10M18 2v10M26 2v10M34 2v10"/></g><g fill="#aaa"><rect x="8" y="24" width="6" height="5"/><rect x="17" y="24" width="6" height="5"/><rect x="26" y="24" width="6" height="5"/><rect x="35" y="24" width="6" height="5"/><rect x="8" y="34" width="6" height="5"/><rect x="17" y="34" width="6" height="5"/><rect x="26" y="34" width="6" height="5"/><rect x="35" y="34" width="6" height="5"/></g></svg>
</div>

<footer class="abs bottom-nav">
  <div class="nav-item" style="left:111px">
    <svg width="62" height="66" viewBox="0 0 48 52"><g fill="none" stroke="#fff" stroke-width="3"><rect x="2" y="8" width="44" height="42"/><path d="M2 18h44M10 2v10M18 2v10M26 2v10M34 2v10"/></g><g fill="#fff"><rect x="8" y="24" width="6" height="5"/><rect x="17" y="24" width="6" height="5"/><rect x="26" y="24" width="6" height="5"/><rect x="35" y="24" width="6" height="5"/><rect x="8" y="34" width="6" height="5"/><rect x="17" y="34" width="6" height="5"/><rect x="26" y="34" width="6" height="5"/><rect x="35" y="34" width="6" height="5"/></g></svg>
    Calender
  </div>
  <div class="nav-item" style="left:344px">
    <svg width="56" height="66" viewBox="0 0 56 56"><g fill="#fff"><rect x="0" y="0" width="16" height="16"/><rect x="20" y="0" width="16" height="16"/><rect x="40" y="0" width="16" height="16"/><rect x="0" y="20" width="16" height="16"/><rect x="20" y="20" width="16" height="16"/><rect x="40" y="20" width="16" height="16"/><rect x="0" y="40" width="16" height="16"/><rect x="20" y="40" width="16" height="16"/><rect x="40" y="40" width="16" height="16"/></g></svg>
    Entity
  </div>
  <div class="nav-item" style="left:551px">
    <svg width="52" height="66" viewBox="0 0 52 66"><g fill="none" stroke="#fff" stroke-width="3.5" stroke-linejoin="round"><path d="M3 3h32l14 14v46H3Z"/><path d="M35 3v14h14M12 30h28M12 40h28M12 50h28"/></g></svg>
    Tasks
  </div>
  <div class="nav-item" style="left:817px">
    <svg width="66" height="66" viewBox="0 0 66 66"><g fill="#fff"><circle cx="33" cy="33" r="20"/><g id="teeth"><rect x="27" y="2" width="12" height="14"/><rect x="27" y="50" width="12" height="14"/><rect x="2" y="27" width="14" height="12"/><rect x="50" y="27" width="14" height="12"/></g><use href="#teeth" transform="rotate(45 33 33)"/></g><circle cx="33" cy="33" r="8" fill="var(--blue)"/></svg>
    Settings
  </div>
  <div class="nav-item" style="left:1078px">
    <svg width="66" height="66" viewBox="0 0 66 66"><g fill="#fff"><path d="M30 10c-12 0-18 10-18 22v12l-6 8h48l-6-8V32c0-12-6-22-18-22Z"/><circle cx="30" cy="58" r="6"/><circle cx="46" cy="12" r="11"/></g><text x="46" y="17" font-size="14" font-weight="500" text-anchor="middle" fill="var(--blue)" font-family="Source Sans 3, sans-serif">1</text></svg>
    Notification
  </div>
</footer>
</body>
</html>
```